Cardboard hanging box designs

I need to get some cardboard boxes made up for trailer wheel bearing kits. They need to be hanging boxes as pictured. The box needs to fit with our existing colour scheme and be clearly evident that it is for trailers. I am after 2 designs, one for "Trailer Bearing Kit" and one for "Marine Bearing Kit".
The Marine Bearing kit box should measure, 180mm High, 120mm Wide, 60mm Deep.
The Trailer Bearing kit box should measure, 180mm high, 120mm Wide, 30mm Deep.
These are all external measurements.

```html
<!DOCTYPE html>
<html lang="en">
<head>
<meta charset="utf-8">
<title>Bearing Kit Hanging Box Panels</title>
<link rel="stylesheet" href="https://fonts.googleapis.com/css2?family=Archivo:wght@800;900&display=swap">
<style>
  :root {
    --paper: #ffffff;
    --stage: #ffffff;
    --fold: #d6d6d6;
    --brand-red: #e8293a;
    --ink: #111111;
    --pattern-grey: #e2e2e2;
    --pattern-grey-soft: #efefef;
  }
  html, body {
    margin: 0;
    padding: 0;
    width: 1200px;
    height: 1039px;
    overflow: hidden;
    background: var(--stage);
  }
  .canvas {
    position: relative;
    width: 1200px;
    height: 1039px;
    font-family: "Archivo", "Arial Black", sans-serif;
  }
  .panel {
    position: absolute;
    background: var(--paper);
    border: 1px solid var(--fold);
    overflow: hidden;
    box-sizing: border-box;
  }
  .panel svg.artwork {
    position: absolute;
    left: 0;
    top: 0;
  }
  .panel--marine { left: 53px; top: 70px; width: 565px; height: 423px; }
  .panel--trailer { left: 128px; top: 544px; width: 424px; height: 423px; }

  .brand {
    position: absolute;
    display: flex;
    align-items: center;
    gap: 7px;
    padding: 8px 12px;
    background: var(--paper);
    transform: translate(-50%, -50%);
    white-space: nowrap;
  }
  .brand__mark {
    width: 14px;
    height: 14px;
    background: var(--brand-red);
  }
  .brand__name {
    font-weight: 900;
    font-size: 24px;
    line-height: 1;
    letter-spacing: 0.5px;
    color: var(--ink);
    text-transform: uppercase;
  }
  .title {
    position: absolute;
    margin: 0;
    line-height: 1;
    white-space: nowrap;
  }
  .title__main {
    display: block;
    font-weight: 900;
    color: var(--brand-red);
    letter-spacing: -0.5px;
  }
  .title__sub {
    display: block;
    font-weight: 800;
    font-size: 29px;
    color: var(--ink);
    margin-top: 4px;
  }
  .panel--marine .brand { left: 285px; top: 96px; }
  .panel--marine .title { left: 182px; top: 182px; }
  .panel--marine .title__main { font-size: 46px; }
  .panel--trailer .brand { left: 213px; top: 94px; }
  .panel--trailer .title { left: 107px; top: 183px; }
  .panel--trailer .title__main { font-size: 46px; }
  .panel--trailer .title__sub { margin-left: 5px; }
</style>
</head>
<body>
<main class="canvas">

  <section class="panel panel--marine" aria-label="Marine bearing kit box panel">
    <svg class="artwork" width="565" height="423" viewBox="0 0 565 423">
      <defs>
        <linearGradient id="compass-fill" x1="0" y1="0" x2="1" y2="1">
          <stop offset="0" stop-color="#f2f2f2"/>
          <stop offset="1" stop-color="#e6e6e6"/>
        </linearGradient>
      </defs>
      <rect class="compass-pattern" x="0" y="94" width="565" height="242" fill="url(#compass-fill)" role="img" aria-label="Faint grey compass rose pattern"/>
      <rect class="nautical-band" x="0" y="40" width="565" height="54" fill="var(--pattern-grey-soft)" role="img" aria-label="Grey band of coral, ships, starfish, shells, anchors and lighthouses"/>
      <rect class="nautical-band" x="0" y="336" width="565" height="53" fill="var(--pattern-grey-soft)" role="img" aria-label="Grey band of coral, ships, starfish, shells, anchors and lighthouses"/>
      <line class="fold" x1="142" y1="0" x2="142" y2="423" stroke="var(--fold)" stroke-width="1"/>
      <line class="fold" x1="424" y1="0" x2="424" y2="423" stroke="var(--fold)" stroke-width="1"/>
      <g class="rules" stroke="var(--brand-red)" stroke-width="2">
        <line x1="0" y1="40" x2="565" y2="40"/>
        <line x1="0" y1="94" x2="565" y2="94"/>
        <line x1="0" y1="336" x2="565" y2="336"/>
        <line x1="0" y1="389" x2="565" y2="389"/>
      </g>
      <rect class="anchor-illustration" x="332" y="266" width="126" height="146" rx="10" fill="#222222" role="img" aria-label="Black anchor wrapped in rope"/>
    </svg>
    <div class="brand"><span class="brand__mark"></span><span class="brand__name">Ravel Parts</span></div>
    <h2 class="title"><span class="title__main">MARINE</span><span class="title__sub">BEARING KIT</span></h2>
  </section>

  <section class="panel panel--trailer" aria-label="Trailer bearing kit box panel">
    <svg class="artwork" width="424" height="423" viewBox="0 0 424 423">
      <polygon class="tyre-tracks" points="0,300 0,195 330,0 424,0 424,110 150,423 40,423" fill="var(--pattern-grey-soft)" role="img" aria-label="Diagonal grey tyre track pattern"/>
      <line class="fold" x1="70" y1="0" x2="70" y2="423" stroke="var(--fold)" stroke-width="1"/>
      <line class="fold" x1="353" y1="0" x2="353" y2="423" stroke="var(--fold)" stroke-width="1"/>
      <g class="rules" stroke="var(--brand-red)" stroke-width="2">
        <line x1="0" y1="39" x2="424" y2="39"/>
        <line x1="0" y1="92" x2="424" y2="92"/>
        <line x1="0" y1="335" x2="424" y2="335"/>
        <line x1="0" y1="387" x2="424" y2="387"/>
      </g>
      <circle class="wheel-illustration" cx="297" cy="365" r="86" fill="#222222" role="img" aria-label="Black trailer wheel with spoked rim"/>
    </svg>
    <div class="brand"><span class="brand__mark"></span><span class="brand__name">Ravel Parts</span></div>
    <h2 class="title"><span class="title__main">TRAILER</span><span class="title__sub">BEARING KIT</span></h2>
  </section>

</main>
</body>
</html>
```